'Ormel Property Development' Business Card

Business Card Features:

High Quality (potentially textured) thick card - preference is white textured card

Logo (supplied)

We plan to use the vertical logo as the main logo. But i am happy for people to use either if they find it works better for the design of the card.

The building icon and also the insert to the 'E' is in a metallic finish, i think this should be finished in a metallic embossed or raised style.
Updates

Please note i have attached both a horizontal and Vertical Logo for your reference. We plan to use the vertical logo as the main logo. But i am happy for people to use either if they find it works better for the design of the card.

Please note i am considering having the cards made on stainless steel. This introduces the option of having cut outs in the card and etching or printing for the design. If you have a good concept for this please submit.

http://www.tinquarry.example/black-metal-cards# this is a site that makes the metal cards to offer some direction . . . . Please note i am basic the selection o the best design, if that means normal print cards on paper then this is what i will choose. But there are some great options with the metal. Thanks.

Industry/Entity Type

Building

Requirements
Must have
• Helvetica font to details side of card - logo as supplied to opposite side.

Card Details:

Darrow Pketts
Managing Director

+61 487 263 518
+61 3 6172 4809

PO Box 73
Bentleigh, VIC 3024

darrow@ormel.example

www.ormel.example

```html
<!DOCTYPE html>
<html lang="en">
<head>
<meta charset="utf-8">
<title>Ormel Property Development – Business Card</title>
<link rel="stylesheet" href="https://fonts.googleapis.com/css2?family=Arimo:wght@400;700&display=swap">
<style>
  :root {
    --backdrop: #d6d6d6;
    --card-white: #ffffff;
    --charcoal: #5d5e5f;
    --charcoal-deep: #4f5051;
    --mid-grey: #9c9d9e;
    --light-grey: #bdbebf;
    --text-dark: #3d3d3d;
    --text-body: #555556;
    --rule: #7a7a7a;
    --icon-fill: #a8a29f;
  }
  * { box-sizing: border-box; margin: 0; padding: 0; }
  html, body {
    width: 1200px; height: 725px; overflow: hidden;
    background: var(--backdrop);
    font-family: "Arimo", Helvetica, Arial, sans-serif;
  }
  .card {
    position: absolute; top: 208px;
    width: 540px; height: 310px; overflow: hidden;
    box-shadow: 0 6px 18px rgba(0,0,0,0.18);
  }
  .card--details { left: 40px; background: var(--card-white); }
  .card--brand { left: 620px; background: var(--charcoal); }

  /* wordmark */
  .wordmark { position: absolute; display: flex; align-items: center; gap: 12px; font-weight: 700; }
  .wordmark__square { width: 14px; height: 14px; background: currentColor; }
  .wordmark__text { line-height: 1; }
  .wordmark__name { display: block; font-size: 38px; letter-spacing: 1px; }
  .wordmark__sub { display: block; font-size: 11px; letter-spacing: 0.8px; margin-top: 5px; text-transform: uppercase; }
  .card--details .wordmark { left: 36px; top: 26px; color: var(--charcoal); }
  .card--brand .wordmark { left: 150px; top: 100px; color: var(--card-white); }
  .card--brand .wordmark__name { font-size: 64px; letter-spacing: 2px; }
  .card--brand .wordmark__sub { font-size: 15px; margin-top: 8px; }

  .divider { position: absolute; left: 36px; right: 36px; top: 108px; height: 1px; background: var(--rule); }

  .address { position: absolute; left: 36px; top: 128px; color: var(--text-body); font-size: 14px; line-height: 1.3; font-style: normal; }
  .address__web { margin-top: 10px; font-weight: 700; color: var(--text-dark); }

  .person { position: absolute; right: 36px; top: 122px; text-align: right; }
  .person__name { font-size: 19px; font-weight: 700; color: var(--text-dark); }
  .person__title { font-size: 17px; color: var(--text-body); margin-top: 3px; }

  .contacts { position: absolute; right: 36px; top: 174px; list-style: none; }
  .contacts__item { display: flex; align-items: center; justify-content: flex-end; gap: 10px; height: 26px; font-size: 15px; color: var(--text-body); }
  .contacts__icon { width: 22px; height: 22px; }

  .footer-band { position: absolute; left: 0; bottom: 0; width: 540px; height: 42px; }
  .brand-band { position: absolute; left: 0; bottom: 0; width: 540px; height: 70px; }
</style>
</head>
<body>

<section class="card card--details" aria-label="Business card, details side">
  <div class="wordmark">
    <span class="wordmark__square"></span>
    <span class="wordmark__text">
      <span class="wordmark__name">ORMEL</span>
      <span class="wordmark__sub">Property Development</span>
    </span>
  </div>

  <div class="divider"></div>

  <address class="address">
    <p>PO Box 73, Bentleigh,</p>
    <p>VIC 3024</p>
    <p class="address__web">www.ormel.example</p>
  </address>

  <div class="person">
    <p class="person__name">Darrow Pketts</p>
    <p class="person__title">Managing Director</p>
  </div>

  <ul class="contacts">
    <li class="contacts__item">0487 263 518
      <svg class="contacts__icon" viewBox="0 0 22 22" aria-hidden="true">
        <circle cx="11" cy="11" r="11" fill="var(--icon-fill)"/>
        <rect x="7.5" y="4.5" width="7" height="13" rx="1.2" fill="none" stroke="#fff" stroke-width="1.3"/>
        <circle cx="11" cy="15.3" r="0.8" fill="#fff"/>
      </svg>
    </li>
    <li class="contacts__item">1800 614 207
      <svg class="contacts__icon" viewBox="0 0 22 22" aria-hidden="true">
        <circle cx="11" cy="11" r="11" fill="var(--icon-fill)"/>
        <path d="M7 5.5 l2.3 0 l1 3 l-1.5 1.2 q1.2 2.4 3.5 3.5 l1.2 -1.5 l3 1 l0 2.3 q-1 1.5 -3 1 q-6 -2 -7.5 -8 q-0.3 -1.6 1 -2.5z" fill="#fff"/>
      </svg>
    </li>
    <li class="contacts__item">darrow@ormel.example
      <svg class="contacts__icon" viewBox="0 0 22 22" aria-hidden="true">
        <circle cx="11" cy="11" r="11" fill="var(--icon-fill)"/>
        <rect x="5" y="7" width="12" height="8.5" fill="none" stroke="#fff" stroke-width="1.3"/>
        <path d="M5 7 L11 12 L17 7" fill="none" stroke="#fff" stroke-width="1.3"/>
      </svg>
    </li>
  </ul>

  <svg class="footer-band" viewBox="0 0 540 42" aria-hidden="true">
    <rect x="0" y="0" width="540" height="42" fill="var(--mid-grey)"/>
    <polygon points="0,10 300,10 282,42 0,42" fill="var(--charcoal)"/>
    <polygon points="318,10 540,10 540,42 300,42" fill="var(--light-grey)"/>
    <polygon points="300,10 318,10 300,42 282,42" fill="var(--card-white)"/>
  </svg>
</section>

<section class="card card--brand" aria-label="Business card, brand side">
  <div class="wordmark">
    <span class="wordmark__square"></span>
    <span class="wordmark__text">
      <span class="wordmark__name">ORMEL</span>
      <span class="wordmark__sub">Property Development</span>
    </span>
  </div>

  <svg class="brand-band" viewBox="0 0 540 70" aria-hidden="true">
    <polygon points="330,40 540,10 540,70 290,70" fill="var(--mid-grey)"/>
    <polygon points="0,70 0,55 300,55 290,70" fill="var(--charcoal-deep)"/>
  </svg>
</section>

</body>
</html>
```